Herbal Tincture Product Packaging

Rebrand herbal product labels for use on 2 oz tincture bottles - current packaging attached. (no box needed). Bottles are frosted glass Boston rounds 2 oz with silver cap dropper. logo options attached. 3 products/varieties: Harbor, Lantern, Meadow - would really also like a visual icon to represent product variety at a glance, in addition to name.
Please see guidelines below:
Label Material:
Base- polyester, BOPP, or other non-vinyl synthetics Lamination- matte or gloss Backing- white or kraft, no transparent
Spooling:
Rewind direction #4, 3” core, not more that 1200 per roll, not less than 500 per roll Please include 5-10% overage (ex. if you have 500 units on order, please print 525-550 labels).
Sizing:
2oz. ABR- >/= 2” H x 4.5” W
Suggested guidelines review:
https://www.krvl.org/files/Document%20Library/KRVL%20Guidance%20Documents/Packaging%20and%20Labeling/KRVL%20Guidance_Herbal%20Supplements%20Labeling%20Guide%20(Revised%202021).pdf
Target Market(s)
Health Conscious age 24+
Industry/Entity Type
holistic health care
Colors
Look and feel

```html
<!DOCTYPE html>
<html lang="en">
<head>
<meta charset="utf-8">
<title>Herbal Tincture Labels – Harbor, Meadow, Lantern</title>
<link rel="stylesheet" href="https://fonts.googleapis.com/css2?family=Michroma&family=Open+Sans:wght@700&display=swap">
<style>
  :root{
    --page:#f3f3f3;
    --label-bg:#f6f3f8;
    --brand:#4a1f1f;
    --harbor:#9b4fb0;
    --harbor-deep:#6a1d7e;
    --harbor-mark:#3d9a4a;
    --meadow:#b6c9a2;
    --meadow-deep:#c89a5c;
    --meadow-mark:#d9a77c;
    --lantern:#b57b82;
    --lantern-deep:#7e2a63;
    --lantern-mark:#e9bb9c;
    --white:#ffffff;
  }
  *{box-sizing:border-box;margin:0;padding:0}
  html,body{width:1200px;height:1200px;overflow:hidden;background:var(--page)}
  .sheet{width:1200px;height:1200px;display:flex;justify-content:center;align-items:center;gap:50px}
  .label{position:relative;width:330px;height:440px;background:var(--label-bg);display:flex;overflow:hidden}
  .label-texture{position:absolute;inset:0 0 0 56px;background:linear-gradient(160deg,#fbf9fc,#ece4f0)}
  .variant-band{position:relative;width:56px;height:100%;display:flex;align-items:flex-end;justify-content:center;padding-bottom:40px}
  .variant-name{writing-mode:vertical-rl;transform:rotate(180deg);font-family:"Michroma",sans-serif;font-size:26px;letter-spacing:14px;color:var(--white)}
  .label-body{position:relative;flex:1;display:flex;flex-direction:column;align-items:center;padding:22px 50px 0 0}
  .variant-icon{width:150px;height:150px;border-radius:50%;border:5px solid var(--brand)}
  .brand{margin-top:26px;font-family:"Open Sans",sans-serif;font-size:34px;font-weight:700;letter-spacing:6px;color:var(--brand);line-height:1}
  .drop{margin-top:22px}
  .size-pill{margin-top:18px;display:flex;border-radius:4px;overflow:hidden;font-family:"Open Sans",sans-serif;font-weight:700;font-size:11px;color:var(--white)}
  .size-pill span{padding:3px 7px}
  .claim{margin-top:6px;font-family:"Open Sans",sans-serif;font-weight:700;font-size:11px;letter-spacing:1px;color:var(--brand)}
  .forms{position:absolute;right:10px;top:70px;display:flex;flex-direction:column;gap:10px}
  .forms span{writing-mode:vertical-rl;transform:rotate(180deg);font-family:"Open Sans",sans-serif;font-weight:700;font-size:11px;letter-spacing:1px;color:var(--white);padding:8px 4px;border-radius:6px;text-align:center}
  .forms .tinctures{height:112px}.forms .tonics{height:88px}.forms .teas{height:60px}

  .harbor .variant-band,.harbor .forms span{background:var(--harbor)}
  .harbor .variant-icon{background:radial-gradient(circle,var(--harbor-mark),var(--harbor-deep));border-color:var(--harbor-deep)}
  .harbor .size-pill span:first-child{background:var(--harbor-mark)}
  .harbor .size-pill span:last-child{background:var(--harbor-deep)}
  .meadow .variant-band,.meadow .forms span{background:var(--meadow)}
  .meadow .variant-icon{background:radial-gradient(circle,var(--meadow-mark),#6b2a4a)}
  .meadow .size-pill span:first-child{background:#b9b57a}
  .meadow .size-pill span:last-child{background:var(--meadow-deep)}
  .lantern .variant-band,.lantern .forms span{background:var(--lantern)}
  .lantern .variant-icon{background:radial-gradient(circle,var(--lantern-mark),#6b2a4a)}
  .lantern .size-pill span:first-child{background:var(--lantern-deep)}
  .lantern .size-pill span:last-child{background:var(--lantern)}
</style>
</head>
<body>
<main class="sheet">

  <section class="label harbor">
    <div class="label-texture" role="img" aria-label="Faint lilac contour-line pattern"></div>
    <div class="variant-band"><span class="variant-name">HARBOR</span></div>
    <div class="label-body">
      <div class="variant-icon" role="img" aria-label="Round green and purple botanical variety emblem"></div>
      <div class="brand">FERN</div>
      <svg class="drop" width="48" height="72" viewBox="0 0 48 72"><path d="M24 2 C30 24 46 36 46 50 A22 22 0 0 1 2 50 C2 36 18 24 24 2Z" fill="#8e1fb0"/></svg>
      <div class="size-pill"><span>2 OZ</span><span>60ML</span></div>
      <div class="claim">HERBAL SUPPORT</div>
    </div>
    <div class="forms"><span class="tinctures">TINCTURES</span><span class="tonics">TONICS</span><span class="teas">TEAS</span></div>
  </section>

  <section class="label meadow">
    <div class="label-texture" role="img" aria-label="Faint lilac contour-line pattern"></div>
    <div class="variant-band"><span class="variant-name">MEADOW</span></div>
    <div class="label-body">
      <div class="variant-icon" role="img" aria-label="Round peach, sage and plum botanical variety emblem"></div>
      <div class="brand">FERN</div>
      <svg class="drop" width="48" height="72" viewBox="0 0 48 72"><path d="M24 2 C30 24 46 36 46 50 A22 22 0 0 1 2 50 C2 36 18 24 24 2Z" fill="#8a9b78"/></svg>
      <div class="size-pill"><span>2 OZ</span><span>60ML</span></div>
      <div class="claim">HERBAL SUPPORT</div>
    </div>
    <div class="forms"><span class="tinctures">TINCTURES</span><span class="tonics">TONICS</span><span class="teas">TEAS</span></div>
  </section>

  <section class="label lantern">
    <div class="label-texture" role="img" aria-label="Faint lilac contour-line pattern"></div>
    <div class="variant-band"><span class="variant-name">LANTERN</span></div>
    <div class="label-body">
      <div class="variant-icon" role="img" aria-label="Round peach, sage and plum botanical variety emblem"></div>
      <div class="brand">FERN</div>
      <svg class="drop" width="48" height="72" viewBox="0 0 48 72"><path d="M24 2 C30 24 46 36 46 50 A22 22 0 0 1 2 50 C2 36 18 24 24 2Z" fill="#d8a0a8"/></svg>
      <div class="size-pill"><span>2 OZ</span><span>60ML</span></div>
      <div class="claim">HERBAL SUPPORT</div>
    </div>
    <div class="forms"><span class="tinctures">TINCTURES</span><span class="tonics">TONICS</span><span class="teas">TEAS</span></div>
  </section>

</main>
</body>
</html>
```